E-book design and layout (healthcare emergency carts)

I have copy for a small e-book/whitepaper that i need put into a cool print/ebook format. It focuses on the importance of effective use and preparedness for your Crash Cart in a hospital setting. We are a manufacturer of crash carts and would like to provide some insight on how to better utilize them.The copy is attached "Pendravex Ebook" I would just like it to look pretty. Here are photos of the product being talked about
Target Market(s)
Healthcare and professional Buyers for hospitals
Industry/Entity Type
Healthcare
Look and feel

```html
<!DOCTYPE html>
<html lang="en">
<head>
<meta charset="utf-8">
<title>Pendravex Ebook – Crash Cart Preparedness</title>
<link href="https://fonts.googleapis.com/css2?family=Open+Sans:ital,wght@0,400;0,600;0,700;0,800;1,400&display=swap" rel="stylesheet">
<style>
:root{
  --red:#e5202e;
  --red-dark:#c8131f;
  --pink:#f5dfe2;
  --ink:#2b2b2b;
  --muted:#555;
  --paper:#ffffff;
  --stage:#eeeeef;
  --grey-box:#e3e3e4;
}
*{box-sizing:border-box;margin:0;padding:0}
html,body{width:1200px;height:3000px;overflow:hidden}
body{background:var(--stage);font-family:"Open Sans",Arial,sans-serif;color:var(--ink);position:relative}
.page{position:absolute;width:500px;height:690px;background:var(--paper);box-shadow:0 4px 14px rgba(0,0,0,.18);overflow:hidden}
.row1{top:30px}.row2{top:760px}.row3{top:1490px}.row4{top:2220px}
.left{left:70px}.right{left:630px}

/* brand mark */
.brand{display:inline-block;background:var(--red);color:#fff;font-weight:800;letter-spacing:.5px;text-transform:uppercase}
.brand-sm{position:absolute;top:22px;right:26px;font-size:10px;padding:4px 7px}

/* header/footer bands */
.band{position:absolute;height:7px;background:var(--red);clip-path:polygon(2% 0,100% 0,98% 100%,0 100%)}
.band-top{top:30px;left:24px;width:380px}
.band-bottom{bottom:40px;left:52px;width:400px}

.content{position:absolute;top:62px;left:34px;right:34px;bottom:60px;font-size:8.2px;line-height:1.5}
.content p{margin-bottom:8px;text-align:justify}
.section-head{display:flex;align-items:center;gap:6px;margin:10px 0 8px;font-weight:800;font-size:11px;text-transform:uppercase;color:#222}
.section-head .num{background:var(--red);color:#fff;font-size:10px;padding:2px 9px;clip-path:polygon(10% 0,100% 0,90% 100%,0 100%)}
.section-head.mixed{text-transform:none}
ul.dots{list-style:none;margin:0 0 8px 18px}
ul.dots li{position:relative;padding-left:12px;margin-bottom:4px}
ul.dots li::before{content:"";position:absolute;left:0;top:4px;width:4px;height:4px;border-radius:50%;background:var(--red)}
ul.black li::before{background:#222}
ul.italic li{font-style:italic;font-size:7.4px}
.red{color:var(--red);font-weight:700}

/* table */
table.factors{width:100%;border-collapse:collapse;font-size:7.4px;line-height:1.35;margin-bottom:10px}
table.factors th{color:var(--red);font-weight:700;text-align:left;padding:3px 4px}
table.factors td{padding:5px 4px;vertical-align:top;border-top:1px solid #fff}
table.factors tr.shade td{background:var(--pink)}
table.factors td:first-child{font-weight:700}

/* covers */
.cover{background:var(--paper)}
.cover .spine-edge{position:absolute;top:0;bottom:0;left:0;width:8px;background:var(--red)}
.cover .bottom-edge{position:absolute;left:0;right:0;bottom:0;height:8px;background:var(--red)}
.cover .brand-lg{position:absolute;top:44px;right:44px;font-size:30px;padding:10px 18px}
.back .brand-lg{position:absolute;left:150px;top:440px;font-size:30px;padding:10px 18px}
.back .spine-edge{left:auto;right:0}
.cover-photo{position:absolute;top:150px;left:60px;right:30px;height:360px;border-radius:4px;background:linear-gradient(160deg,#f4f6f8 0%,#bcd6e6 45%,#3a7fc2 80%,#e9eef2 100%)}
.cover-title{position:absolute;left:60px;bottom:70px;font-size:9px;color:var(--muted);letter-spacing:1px;text-transform:uppercase;font-weight:600}

.photo-cart{background:linear-gradient(180deg,#f2f3f5 0%,#d9dde3 40%,#4b7fc4 70%,#eef0f2 100%);border-radius:3px}
.photo-cart.redcart{background:linear-gradient(180deg,#f2f3f5 0%,#d9dde3 35%,#c8202b 70%,#eef0f2 100%)}
.float-img{float:right;width:110px;height:120px;margin:0 0 6px 10px}

.subhead{color:#222;font-weight:700;font-size:8.6px;border-bottom:1px solid var(--red);padding-bottom:2px;margin:4px 0 8px 10px}
.cols{display:flex;gap:20px}
.cols ul{flex:1}
.note{font-style:italic;font-size:7.4px;margin:0 0 8px 10px}
.sources{background:var(--grey-box);border-radius:8px;padding:8px 10px;font-size:7.6px;margin:18px 0}
.sources a{color:#2a4fbf;display:block;margin-top:6px}
.cart-pair{display:flex;justify-content:space-around;margin-top:30px}
.cart-pair div{width:120px;height:170px}
</style>
</head>
<body>

<!-- Back cover -->
<section class="page cover back row1 left">
  <div class="spine-edge"></div>
  <div class="bottom-edge"></div>
  <span class="brand brand-lg">Pendravex</span>
</section>

<!-- Front cover -->
<section class="page cover row1 right">
  <div class="spine-edge"></div>
  <div class="bottom-edge"></div>
  <span class="brand brand-lg">Pendravex</span>
  <div class="cover-photo" role="img" aria-label="Photo of three clinicians in blue scrubs working around a blue emergency crash cart"></div>
  <div class="cover-title">Pendravex Ebook · Crash Cart Preparedness</div>
</section>

<!-- Page 1 -->
<section class="page row2 left">
  <div class="band band-top"></div><span class="brand brand-sm">Pendravex</span>
  <div class="content">
    <h2 class="section-head"><span class="num">1.</span>Pendravex knows healthcare carts</h2>
    <div class="float-img photo-cart" role="img" aria-label="Product photo of a white and blue crash cart with drawers"></div>
    <p>Since the company's founding in 1929, Pendravex has drawn its innovation from a deep understanding of customer needs to drive recognized global leadership in storage and transport solutions. Today our mission continues: to make the world more organized and efficient. Our design teams are driven to develop novel solutions that make our customers more efficient in their every day processes. Pendravex's line of crash carts are one example of this determination.</p>
    <p>By definition, a crash cart is a mobile cart stocked with emergency supplies, equipment and medications that are used in life support protocols. These carts are built to move with ease but big enough to hold essential supplies. Here we will walk you through what you need to know about crash carts and what you can do to increase the organization of the supplies in your crash carts.</p>
    <h2 class="section-head"><span class="num">2.</span>Why a crash cart?</h2>
    <p>Any environment where a patient may experience a medical emergency needs to have the equipment to deal with that emergency efficiently. Having all of the supplies, equipment and medications organized in one convenient location that can be quickly moved to a needed location is the reason that facilities invest in crash carts. Crash carts are designed to support treatment at the moment there is an emergency and need to be able to get to patients quickly. The inventory list needed within the cart itself differ based on their placement within a facility and the department it is placed in, but the general crash cart contains the same necessary tools and supplies.</p>
    <h2 class="section-head"><span class="num">3.</span>Who needs a crash cart?</h2>
    <p>Any department that handles patients who have the potential to have an unexpected decline in their health should have a crash cart. State regulatory agencies require these types of facilities to have a crash cart, the number of carts a facility should have, however, is not defined, but careful consideration can help determine what number is right for you. Considerations:</p>
    <ul class="dots">
      <li>Accessibility to crash cart – how far/how long would it take to get a cart to the code</li>
      <li>What procedures are being performed – what is the potential for deterioration</li>
      <li>Patient acuity level – what is the likelihood more than one patient would need a crash cart at the same time</li>
      <li>911 response time – what needs to be done during this time period</li>
    </ul>
  </div>
  <div class="band band-bottom"></div>
</section>

<!-- Page 2 -->
<section class="page row2 right">
  <div class="band band-top"></div><span class="brand brand-sm">Pendravex</span>
  <div class="content">
    <p>Some places where crash carts are required include hospitals, outpatient surgery centers, urgent care centers, and centers where conscious sedation is often performed on patients. This is just a small sampling of the facilities that require crash carts; others include nursing homes that treat for cardiac arrest, and physician offices that perform specific forms of stress testing. Essentially, a facility needs the number of carts necessary to meet potential patient care needs. For an office, that may be one, for a hospital that is a fleet.</p>
    <h2 class="section-head"><span class="num">4.</span>Consequences of bad crash cart practice</h2>
    <p>Crash carts need to be ready to take on an emergency is yours? If the answer is no, then you might have some work to do. If your crash cart isn't being utilized efficiently, there are a few underlying reasons as to why that is. The first is that the crash cart you invested in isn't a proper match for your facility. The second revolves around supply management. Having the right supplies on a crash cart is vital because caregivers often need them immediately for the patient to survive. In a 12-month data review of hospital data, the Regional Patient Safety Board found 56 reports that showed emergency response calls where supplies or equipment were missing or expired. Of the 56 statements, 35 referenced issues with crash carts themselves and 21 referenced problems with unavailable supplies or other supply management issues.</p>
    <h2 class="section-head"><span class="num">5.</span>Contributing factors to failure</h2>
    <table class="factors">
      <tr><th>Contributing Factor</th><th>Implication</th><th>Feature</th><th>How it helps</th></tr>
      <tr class="shade"><td>Missing, expired, damaged, contaminated, and unavailable equipment, supplies or medications</td><td>Not having the right medications and equipment available in these high stress situations can lead to adverse outcomes</td><td>Customer implemented checklist</td><td>Utilizing a checklist will make sure that all necessary medications are available in the critical moments when a crash cart is in use</td></tr>
      <tr class="shade"><td>Drained batteries on equipment or equipment failure</td><td>Not having fully charged equipment or a place to power them leaves them useless</td><td>Pendravex cart equipped with power strip</td><td>Our power strip consolidates equipment cords, to provide ample outlets and only 1 disconnect from wall, helping ensure equipment is charged and ready for an emergency situation</td></tr>
      <tr class="shade"><td>Unsecured carts or carts that have been tampered with – carts secured with heavy duty tape and/or padlocks, preventing immediate access</td><td>Not having unhindered, immediate access to a crash cart impedes life saving actions in critical moments</td><td>Pendravex cart designed with passive locking systems utilizing tamper-evident seals</td><td>Our tamper evident seal both ensures that the contents of the cart have not been changed since they were filled and also allow easy access to first responders</td></tr>
    </table>
  </div>
  <div class="band band-bottom"></div>
</section>

<!-- Page 3 -->
<section class="page row3 left">
  <div class="band band-top"></div><span class="brand brand-sm">Pendravex</span>
  <div class="content">
    <table class="factors">
      <tr><td>Staff is unfamiliar with the procedures for using the crash cart when responding to a life-threatening emergency</td><td>Being unfamiliar with what is contained within and how to use a crash cart is one large reason that crucial time is lost in a life saving emergency</td><td>User Guide and trainings</td><td>Pendravex provides user guides and trainings on how to use a cart effectively, and knowing that will help make users more effective</td></tr>
      <tr class="shade"><td>Response time – moments are critical during these events, the initial moments being the most critical to successfully stabilizing a patient</td><td>Time wasted struggling with transporting the cart, or waiting to access a supply or medication is time that can be spent attending to the patient</td><td>Pendravex Steadline crash cart proprietary design features help reduce waste in delivery and access,</td><td>Pendravex's Steadline crash cart designed with 5th wheel steering, helps quicken transport, simultaneous access points, allow clinicians access to their contents sooner</td></tr>
    </table>
    <p>Each of these issues has been proven to delay healthcare professionals, which creates an immediate patient safety risk. By ensuring the proper cart and supplies are available, facilities can better serve the community and have an easier time handling emergencies. By improving efficiency, facilities can offer better service, limit delays, and have an improvement in patient outcomes following a crisis.</p>
    <h2 class="section-head"><span class="num">6.</span>Addressing these can help mitigate risks</h2>
    <p>Safety Actions to Consider: Medical emergencies tend to create a sense of madness and confusion. These feelings may be increased and run rampant if the emergency equipment used to rescue the patient is not ready when it needs to be. This is where the crash cart comes in, it ensures that the needed supplies are prepared in these tense emergency situations. Here are some ways to make sure that your cart is ready.</p>
    <p>Make a risk assessment: &nbsp;Identify the risk areas ; drill down to find the issues and where they originated. Risk points can include:</p>
    <ul class="dots">
      <li><span class="red">Staff training:</span> Staff Training and educational needs to identify who responds; ensure that the staff person has appropriate education and training in what needs to be in the cart and how to work it. Mock codes are a valuable exercise to assess training needs</li>
      <li><span class="red">Cart Checks:</span> Identify who should check the crash cart and ensure that it is checked at the beginning of each shift daily and the proper equipment tests are conducted according to manufacturer instructions.</li>
      <li><span class="red">Location:</span> Knowing where carts are stored is extremely important. Having a designated area for each cart ensures that it can be found in a timely manner.</li>
      <li><span class="red">Contents:</span> Contents of a crash cart should be easy to spot and grab in an emergency situation. To do this, invest in an easy to understand labeling system. Having a system to easily find medication can improve the speed at which it is administered. It can also be helpful to include a cart graphic that shows exactly where everything in the cart is located.</li>
    </ul>
  </div>
  <div class="band band-bottom"></div>
</section>

<!-- Page 4 -->
<section class="page row3 right">
  <div class="band band-top"></div><span class="brand brand-sm">Pendravex</span>
  <div class="content">
    <p>Segregate and clearly label pediatric medications, having them separate makes them easier to identify and grab quickly, and help ensures children are not given the wrong form of medication. &nbsp;Consideration should also be given to having a completely separate cart for pediatrics, that can be organized by patient size.</p>
    <h2 class="section-head"><span class="num">7.</span>Implementing an action plan</h2>
    <p>Now that you know what needs to be done, how do you get started? First, strategize. Having a mapped out organization strategy will help make change easier, and is a great way to track your progress. After you have your plan finalized, and all of your stakeholders bought in, implement it, but be flexible to change to tweak to real life situations or other changes over time. This plan should include:</p>
    <ul class="dots">
      <li>Equipment, supply, and medication inventory management plans</li>
      <li>Staff Training to ensure that staff remains proficient</li>
      <li>Emergency Protocols and Drills</li>
      <li>An outline of Individual Responsibilities</li>
    </ul>
    <h2 class="section-head"><span class="num">8.</span>List of contents</h2>
    <p>What is in a crash cart? Here is a basic breakdown of what a crash cart should have on the ready:</p>
    <ul class="dots italic">
      <li>Basic airway equipment including bag valve masks, oral and nasal airways, oxygen masks and nasal cannulas, angled airway forceps</li>
      <li>Intravenous access equipment (or intraosseous) including angiocaths, IV tubing, and IV fluid. If the facility elects to utilize intraosseous access for emergency medications, then a drill and needles must be included.</li>
      <li>Medications utilized in the treatment of cardiac arrest, including epinephrine and amiodarone.</li>
      <li>Medications utilized to treat cardiac dysrhythmias including adenosine, Diltrex®, a beta blocker (usually Metorin®), and Atropine.</li>
      <li>Monitor equipment with a defibrillator or an AED</li>
      <li>Medications to treat allergic reactions such as EpiShot®, Corticel®, and Histanol®</li>
      <li>Aspirin</li>
      <li>Nitroglycerin spray or tablets</li>
    </ul>
    <p>Additionally, carts being utilized for specialized areas may add or subtract from the basic list. Depending upon the specialty of the facility, the following may be added:</p>
    <ul class="dots italic">
      <li>Endotracheal intubation equipment if anesthesia personnel are present in the facility</li>
      <li>Kingsway Airways – in facilities without anesthesia personnel or as a bailout airway for the patient with a difficult airway</li>
      <li>Naloxel – to reverse the effects of narcotics in facilities where narcotics or sedation is used</li>
      <li>Additional antiarrhythmics – particularly in physician offices who do cardiac stress testing</li>
    </ul>
  </div>
  <div class="band band-bottom"></div>
</section>

<!-- Page 5 -->
<section class="page row4 left">
  <div class="band band-top"></div><span class="brand brand-sm">Pendravex</span>
  <div class="content">
    <h2 class="section-head"><span class="num">9.</span>Here is a checklist you can use list the source…</h2>
    <div class="subhead">Equipment</div>
    <ul class="dots black">
      <li>Airway (oral and nasal) all sizes</li>
      <li>Angled airway forceps, large and small</li>
      <li>Kingsway Airway set (3) eliminates the need for laryngoscope and endotracheal tubes</li>
      <li>Bag valve mask (adult and pediatric)</li>
      <li>Nasal cannula</li>
      <li>Non-rebreather oxygen face masks (3 sizes)</li>
      <li>IV start packs</li>
      <li>Normal saline solution (1000ml bags)</li>
      <li>IV tubing</li>
      <li>Angiocaths (various sizes)</li>
      <li>normal saline flush syringes (3)</li>
      <li>Gauze</li>
      <li>Alcohol preps</li>
      <li>Monitor with defibrillator (preferred) or AED</li>
      <li>Syringe nasal adaptor (nasal Naloxel atomizer)</li>
      <li>Personal Protective Equipment (Gloves, Masks, garment)</li>
    </ul>
    <p class="note">A checklist confirming everything that should be on the cart</p>
    <div class="subhead">Drugs <span style="font-weight:400">(list the source or remove the dosages.)</span></div>
    <div class="cols">
      <ul class="dots black">
        <li>Aspirin 81mg Tablets</li>
        <li>Nitroglycerin spray or 0.4mg tablets</li>
        <li>Dextrose 50% (dextrose 25% if treating pediatrics)</li>
        <li>Naloxel 1mg/ml (6)</li>
        <li>Epinephrine 1:10,000 Syrinject™ (3)</li>
        <li>Atropine Sulfate 1mg Syrinject™ (3)</li>
        <li>Amiodarone 150mg Vial (4)</li>
        <li>EpiShot® (2)</li>
      </ul>
      <ul class="dots black">
        <li>EpiShot Jr® (2)</li>
        <li>Corticel 125mg vial</li>
        <li>Histanol 50mg vial (2)</li>
        <li>Adenosine 6mg (4)</li>
        <li>Metorin 10mg (2)</li>
        <li>Diltrex 20mg vial (2)</li>
        <li>Procanor (procainamide) 1g in 10 ml 100mg/ml Vial (1)</li>
      </ul>
    </div>
  </div>
  <div class="band band-bottom"></div>
</section>

<!-- Page 6 -->
<section class="page row4 right">
  <div class="band band-top"></div><span class="brand brand-sm">Pendravex</span>
  <div class="content">
    <h2 class="section-head mixed"><span class="num">10.</span>Pendravex Conclusion</h2>
    <p>Picking the right crash cart and organizing it properly can be tough. Don't try and tackle this challenge alone. Reach out to peers at other facilities or through your GPO to build your crash cart plan and then contact the experts at Pendravex to find out which cart is best for your plan. The team at Pendravex also offers consultations in efficiency and supply management to ensure that your cart will be operating at maximum efficiency. To request further information, click the link below and fill out the form. A Pendravex representative will be happy to help.</p>
    <div class="sources">
      Sources:
      <a href="#">https://www.resusguide.example/crash-cart-basics.htm</a>
      <a href="#">https://www.careaccord.example/files/safety-brief-32.pdf</a>
    </div>
    <div class="cart-pair">
      <div class="photo-cart" role="img" aria-label="Product photo of a white and blue crash cart with IV pole and monitor"></div>
      <div class="photo-cart redcart" role="img" aria-label="Product photo of a red and white crash cart with IV pole"></div>
    </div>
  </div>
  <div class="band band-bottom"></div>
</section>

</body>
</html>
```